I want a business card design. the company is an infrastructure development company.

Target Market(s)

Government
real estate investors
real estate clients

Industry/Entity Type

Business

```html
<!DOCTYPE html>
<html lang="en">
<head>
<meta charset="utf-8">
<title>Arden Castellan – Business Card</title>
<link href="https://fonts.googleapis.com/css2?family=Roboto+Condensed:wght@400;700&display=swap" rel="stylesheet">
<style>
  :root {
    --page: #ffffff;
    --card: #ffffff;
    --card-edge: #1a1a1a;
    --ink: #111111;
    --brand-red: #e8101e;
    --brand-cyan: #4fd3f2;
    --stripe-cyan: #5ad8f0;
    --stripe-blue: #1e8be0;
    --stripe-mid: #1565e0;
    --stripe-deep: #0a3de0;
    --band-bright: #ff1430;
    --band-red: #e60008;
    --band-mid: #b80006;
    --band-deep: #9b0000;
    --band-text: #ffffff;
  }
  * { margin: 0; padding: 0; box-sizing: border-box; }
  html, body { width: 1200px; height: 900px; overflow: hidden; background: var(--page); }
  body { position: relative; font-family: "Roboto Condensed", "Arial Narrow", sans-serif; color: var(--ink); }

  .card {
    position: absolute; left: 212px; top: 214px; width: 776px; height: 475px;
    background: var(--card); border: 1px solid var(--card-edge); overflow: hidden;
  }

  .brand { position: absolute; left: 49px; top: 74px; display: flex; align-items: center; gap: 14px; }
  .brand-mark { width: 62px; height: 62px; background: var(--brand-cyan); }
  .brand-name {
    font-weight: 400; font-size: 34px; line-height: 34px; color: var(--brand-red);
    letter-spacing: 1px; text-transform: uppercase;
  }

  .contact { position: absolute; font-size: 21px; line-height: 29px; }
  .contact p { white-space: nowrap; }
  .person { left: 50px; top: 218px; }
  .person-name { font-weight: 700; font-size: 27px; line-height: 32px; }
  .office { left: 471px; top: 151px; }
  .office .gap { margin-top: 12px; }

  .stripe { position: absolute; left: 0; top: 400px; width: 100%; height: 8px; display: flex; }
  .band { position: absolute; left: 0; top: 412px; width: 100%; height: 62px; display: flex; }
  .seg-a { width: 53px; } .seg-b { width: 317px; } .seg-c { width: 56px; } .seg-d { flex: 1; }
  .stripe .seg-a { background: var(--stripe-cyan); }
  .stripe .seg-b { background: var(--stripe-blue); }
  .stripe .seg-c { background: var(--stripe-mid); }
  .stripe .seg-d { background: var(--stripe-deep); }
  .band .seg-a { background: var(--band-bright); }
  .band .seg-b { background: var(--band-red); }
  .band .seg-c { background: var(--band-mid); }
  .band .seg-d { background: var(--band-deep); display: flex; align-items: center; justify-content: center; padding-bottom: 24px; }
  .website { color: var(--band-text); font-weight: 700; font-size: 21px; letter-spacing: 0.3px; }
</style>
</head>
<body>
  <div class="card">
    <div class="brand">
      <div class="brand-mark"></div>
      <div class="brand-name">Arden<br>Castellan</div>
    </div>

    <div class="contact person">
      <p class="person-name">Kolade Ajibola</p>
      <p>MD.</p>
      <p>+234 8031245790</p>
      <p>+234 7052819364</p>
      <p>kolade@ardencastellan.com</p>
    </div>

    <div class="contact office">
      <p>ARDEN CASTELLAN</p>
      <p>12 Harmattan Close</p>
      <p>Off Alder Link Road</p>
      <p>Ikeja Lagos, Nigeria</p>
      <p class="gap">+234 14937215</p>
      <p>+234 7068214539</p>
      <p>info@ardencastellan.com</p>
    </div>

    <div class="stripe">
      <div class="seg-a"></div><div class="seg-b"></div><div class="seg-c"></div><div class="seg-d"></div>
    </div>
    <div class="band">
      <div class="seg-a"></div><div class="seg-b"></div><div class="seg-c"></div>
      <div class="seg-d"><span class="website">www.ardencastellan.com</span></div>
    </div>
  </div>
</body>
</html>
```